Redesigning Web Pages

I need to redesign a section on my website:
http://kelmor.tv-brosk.com/en/pinecresthall
The complete (Pinecrest Hall) section needs to be redesigned.
The works involves designing only. I have my own development team. You would need to provide me with the designing (psd) files at the end of the project.
Please go through the whole section so that you can see the pages that needs to be redesigned (Note: you can create a demo account to see the inner pages, its ok as this link is on the development server). Again, to be clear, I need only to redesign this section (including its sub pages, like registration, user profile page, etc), not the whole website. Of course, the main page to be designed would be the section "main page" the other inner pages are to match the design of the main section page.
All features, functions, and facilities provided on the section are to remain the same.
The design needs to match the current website format. Keep in mind the look and feel information I have provided for this section. Note: Please view the highlighted area in the attached file. This is the area that needs to be redesigned.
The design would be selected based on the creativity of the designer and understanding of what needs to be done.

```html
<!DOCTYPE html>
<html lang="en">
<head>
<meta charset="utf-8">
<title>Kelmor – Pinecrest Hall</title>
<link rel="stylesheet" href="https://fonts.googleapis.com/css2?family=Open+Sans:wght@400;600;700&family=Baloo+2:wght@700;800&display=swap">
<style>
:root{
  --header-top:#4d5686;
  --header-mid:#6a74a6;
  --nav-dark:#454e7c;
  --nav-light:#5d6796;
  --nav-active-text:#e6f0a0;
  --page-grey:#eeeef1;
  --white:#ffffff;
  --panel-border:#8f95c0;
  --panel-head-a:#7a82bb;
  --panel-head-b:#5a6199;
  --ribbon:#d9569a;
  --link-navy:#1f2a6b;
  --body-text:#222222;
  --divider:#d7d9e4;
  --tab-dark:#2e2e2e;
  --tab-active:#9fb2ff;
  --alert-red:#cc0000;
  --footer-a:#3f4775;
  --footer-b:#59628f;
  --icon-dark:#3a3a3a;
}
*{box-sizing:border-box;margin:0;padding:0}
html,body{width:1023px;height:1200px;overflow:hidden}
body{position:relative;background:var(--white);font-family:"Open Sans",Arial,sans-serif;color:var(--body-text)}
.abs{position:absolute}

/* header */
.site-header{position:absolute;left:0;top:0;width:1023px;height:152px;
  background:linear-gradient(180deg,var(--header-top),var(--header-mid) 60%,#5a6496)}
.header-glow{position:absolute;left:230px;top:0;width:440px;height:150px;
  background:linear-gradient(180deg,rgba(255,255,255,.08),rgba(255,255,255,.16));box-shadow:2px 0 6px rgba(0,0,0,.25)}
.brand{position:absolute;left:48px;top:72px;display:flex;align-items:center;gap:10px}
.brand-mark{width:30px;height:30px;border-radius:50%;background:#e2b33a}
.brand-name{font-family:"Open Sans",sans-serif;font-weight:700;font-size:36px;color:var(--white);letter-spacing:1px}
.account-links{position:absolute;left:698px;top:21px;font-size:13px;color:var(--white);display:flex;gap:8px;align-items:center}
.flag{display:inline-block;width:14px;height:10px;background:#c8464a;margin:0 3px}
.caret{width:0;height:0;border-left:6px solid transparent;border-right:6px solid transparent;border-top:7px solid var(--white);margin-left:4px}
.search{position:absolute;left:698px;top:60px;width:274px;height:35px;background:var(--white);border-radius:4px;
  box-shadow:inset 0 1px 3px rgba(0,0,0,.3);font-size:10.5px;color:#444;padding:11px 12px}
.search svg{position:absolute;right:8px;top:6px}
.social{position:absolute;top:111px;width:22px;height:22px;border-radius:50%;background:var(--white);box-shadow:0 1px 2px rgba(0,0,0,.3)}

/* nav */
.main-nav{position:absolute;left:0;top:152px;width:1023px;height:54px;
  background:linear-gradient(180deg,var(--nav-light),var(--nav-dark));border-top:1px solid #3a4270;display:flex;padding-left:39px}
.main-nav a{color:var(--white);text-decoration:none;font-size:13px;line-height:52px;padding:0 11px;border-right:1px solid rgba(255,255,255,.22)}
.main-nav a.active{color:var(--nav-active-text);background:rgba(0,0,0,.14)}
.main-nav a:last-child{border-right:0}

/* hero */
.hero-band{position:absolute;left:0;top:206px;width:1023px;height:296px;background:var(--page-grey);border-bottom:1px solid #d5d5da}
.hero-photo{position:absolute;left:112px;top:223px;width:799px;height:234px;border:2px solid #d7d7dc;
  background:linear-gradient(100deg,#7f8a5a 0%,#e6e2d4 20%,#4fb7e0 38%,#1d8fd6 65%,#1a7ac6 100%);box-shadow:0 14px 18px -8px rgba(0,0,0,.35)}
.hero-caption{position:absolute;right:28px;top:76px;text-align:right;font-family:"Baloo 2",sans-serif;font-weight:800;font-size:22px;line-height:28px;letter-spacing:1px}
.hero-caption .l1{color:#111}
.hero-caption .l2{color:var(--white)}
.hero-arrow{position:absolute;top:321px;width:38px;height:38px;border-radius:50%;background:#3c3c3c;box-shadow:0 1px 3px rgba(0,0,0,.4)}
.hero-arrow svg{position:absolute;left:13px;top:12px}

/* panels */
.panel{position:absolute;top:483px;width:292px;height:404px;background:var(--white);border:1px solid var(--panel-border);border-radius:3px}
.panel-head{height:36px;background:linear-gradient(180deg,var(--panel-head-a),var(--panel-head-b));color:var(--white);
  font-size:18px;text-align:center;line-height:36px;font-weight:600}
.ribbon-wrap{position:absolute;right:-6px;top:-8px;width:86px;height:86px;overflow:hidden}
.ribbon{position:absolute;left:-4px;top:22px;width:130px;height:20px;background:var(--ribbon);color:var(--white);
  font-size:10px;text-align:center;line-height:20px;transform:rotate(45deg);transform-origin:center;box-shadow:0 1px 2px rgba(0,0,0,.3)}
.item{position:absolute;left:8px;width:276px;height:108px;border-bottom:1px solid var(--divider)}
.item.last{border-bottom:0}
.article-text{position:absolute;left:6px;top:14px;width:266px;font-size:11px;line-height:15px;text-align:justify}
.view-more{position:absolute;right:8px;font-size:11px;color:var(--link-navy)}
.thumb{position:absolute;left:6px;top:10px;width:112px;height:80px;border:3px solid #e2e2e6;box-shadow:0 0 2px rgba(0,0,0,.3)}
.thumb-text{position:absolute;left:126px;top:30px;width:152px;font-size:11px;line-height:15px}
.panel-tabs{position:absolute;bottom:-9px;display:flex;gap:3px}
.panel-tab{height:48px;background:linear-gradient(180deg,#8a91c7,#6a72aa);color:var(--white);font-size:15px;line-height:42px;
  text-align:center;border-radius:3px 3px 0 0;box-shadow:0 2px 3px rgba(0,0,0,.35)}

/* member boxes */
.member-box{position:absolute;top:945px;width:229px;height:125px;background:var(--white);border:1px solid #d4d4d8;border-radius:4px;
  box-shadow:0 2px 4px rgba(0,0,0,.12)}
.member-tab{position:absolute;left:10px;top:-16px;height:28px;padding:0 12px;background:var(--tab-dark);color:var(--white);font-size:12px;
  line-height:28px;border-radius:3px}
.member-tab.hot{color:var(--tab-active)}
.member-tab::after{content:"";position:absolute;left:14px;bottom:-6px;border-left:6px solid transparent;border-right:6px solid transparent;border-top:6px solid var(--tab-dark)}
.member{position:absolute;font-size:11px;padding-left:12px}
.member::before{content:"";position:absolute;left:0;top:4px;width:5px;height:5px;border-top:1.5px solid #111;border-right:1.5px solid #111;transform:rotate(45deg)}
.member-link{position:absolute;right:9px;top:94px;font-size:12px;color:var(--alert-red)}

/* footer */
.site-footer{position:absolute;left:0;top:1103px;width:1023px;height:97px;background:linear-gradient(180deg,var(--footer-a),var(--footer-b))}
.footer-links{position:absolute;left:0;top:26px;width:1023px;text-align:center;font-size:11px;color:var(--white)}
.footer-links span{margin:0 6px}
.copyright{position:absolute;left:0;top:61px;width:1023px;text-align:center;font-size:11px;color:var(--white)}
</style>
</head>
<body>

<header class="site-header">
  <div class="header-glow"></div>
  <div class="brand"><span class="brand-mark"></span><span class="brand-name">KELMOR</span></div>
  <div class="account-links">
    <span>Sign in</span><span>|</span><span>Register</span><span>|</span><span>Language : <span class="flag"></span>English</span><span class="caret"></span>
  </div>
  <div class="search">City, Hotel, Name...
    <svg width="22" height="22" viewBox="0 0 22 22"><circle cx="9" cy="9" r="6" fill="#dfe8f5" stroke="#333" stroke-width="2"/><line x1="13.5" y1="13.5" x2="19" y2="19" stroke="#333" stroke-width="3" stroke-linecap="round"/></svg>
  </div>
  <span class="social" style="left:834px"></span>
  <span class="social" style="left:863px"></span>
  <span class="social" style="left:892px"></span>
  <span class="social" style="left:921px"></span>
  <span class="social" style="left:950px"></span>
</header>

<nav class="main-nav">
  <a class="active">Home</a><a>Destinations</a><a>Things to Do</a><a>Hotels</a><a>Weather</a><a>Maps</a><a>Tours</a><a>Travel Photos</a><a>Travel Articles</a><a>Currency Converter</a><a>Pinecrest Hall</a>
</nav>

<section class="hero-band"></section>
<div class="hero-photo" role="img" aria-label="Aerial view of a cove with white sand beach, cliffs and boats on turquoise water">
  <div class="hero-caption"><div class="l1">ORELIO ARE ALSO REPRODUCED</div><div class="l2">EXACT ORIGINAL</div></div>
</div>
<span class="hero-arrow" style="left:85px"><svg width="12" height="14" viewBox="0 0 12 14"><polyline points="9,2 3,7 9,12" fill="none" stroke="#fff" stroke-width="2.5"/></svg></span>
<span class="hero-arrow" style="left:897px"><svg width="12" height="14" viewBox="0 0 12 14"><polyline points="3,2 9,7 3,12" fill="none" stroke="#fff" stroke-width="2.5"/></svg></span>

<!-- Latest Articles -->
<section class="panel" style="left:46px">
  <div class="panel-head">Latest Articles</div>
  <div class="ribbon-wrap"><div class="ribbon">Upload Article</div></div>
  <div class="item" style="top:36px"><p class="article-text">"de Finibus Bonorum et Malorum" by Orelio are also reproduced in their exact original form, accompanied by English versions from the 1914 translation by H. Brantley.</p><span class="view-more" style="top:80px">View more</span></div>
  <div class="item" style="top:144px"><p class="article-text">"de Finibus Bonorum et Malorum" by Orelio are also reproduced in their exact original form, accompanied by English versions from the 1914 translation by H. Brantley.</p><span class="view-more" style="top:80px">View more</span></div>
  <div class="item last" style="top:252px"><p class="article-text">"de Finibus Bonorum et Malorum" by Orelio are also reproduced in their exact original form, accompanied by English versions from the 1914 translation by H. Brantley.</p><span class="view-more" style="top:80px">View more</span></div>
  <div class="panel-tabs" style="left:75px"><span class="panel-tab" style="width:127px">View All Photos</span></div>
</section>

<!-- Travel Stories -->
<section class="panel" style="left:358px">
  <div class="panel-head">Travel Stories &amp; Photos</div>
  <div class="ribbon-wrap"><div class="ribbon">Upload Photo</div></div>
  <div class="item" style="top:36px"><div class="thumb" role="img" aria-label="Paraglider silhouetted against an orange sunset sky" style="background:linear-gradient(180deg,#f2c21a,#e56a0a 70%,#5a2a08)"></div><p class="thumb-text">English versions from the 1914 translation by H. Brantley.</p><span class="view-more" style="top:74px">View more</span></div>
  <div class="item" style="top:144px"><div class="thumb" role="img" aria-label="Two people on beach chairs facing the sea" style="background:linear-gradient(180deg,#3c8fd8,#2fa6e0 55%,#e8dcc0)"></div><p class="thumb-text">English versions from the 1914 translation by H. Brantley.</p><span class="view-more" style="top:74px">View more</span></div>
  <div class="item last" style="top:252px"><div class="thumb" role="img" aria-label="Couple sitting on a terrace overlooking the ocean" style="background:linear-gradient(180deg,#bfe2f5,#4fb4e0 55%,#e8eef2)"></div><p class="thumb-text">English versions from the 1914 translation by H. Brantley.</p><span class="view-more" style="top:74px">View more</span></div>
  <div class="panel-tabs" style="left:75px"><span class="panel-tab" style="width:127px">View All Photos</span></div>
</section>

<!-- Latest Reviews -->
<section class="panel" style="left:681px">
  <div class="panel-head">Latest Reviews</div>
  <div class="ribbon-wrap"><div class="ribbon">Upload Review</div></div>
  <div class="item" style="top:36px"><div class="thumb" role="img" aria-label="Hikers standing on a rocky outcrop" style="background:linear-gradient(180deg,#a9cdea,#8a7a5a 60%,#6a5a40)"></div><p class="thumb-text">English versions from the 1914 translation by H. Brantley.</p><span class="view-more" style="top:74px">View more</span></div>
  <div class="item" style="top:144px"><div class="thumb" role="img" aria-label="Riders on a trail through an autumn forest" style="background:linear-gradient(180deg,#6a7a3a,#a0602a 60%,#5a4a30)"></div><p class="thumb-text">English versions from the 1914 translation by H. Brantley.</p><span class="view-more" style="top:74px">View more</span></div>
  <div class="item last" style="top:252px"><div class="thumb" role="img" aria-label="Jungle valley with palm trees under a blue sky" style="background:linear-gradient(180deg,#8ec0e6,#4a8a3a 45%,#2a5a22)"></div><p class="thumb-text">English versions from the 1914 translation by H. Brantley.</p><span class="view-more" style="top:74px">View more</span></div>
  <div class="panel-tabs" style="left:27px"><span class="panel-tab" style="width:118px">Things to do</span><span class="panel-tab" style="width:58px">Tours</span><span class="panel-tab" style="width:58px">Hotels</span></div>
</section>

<!-- Member boxes -->
<section class="member-box" style="left:38px">
  <span class="member-tab">Recent Register Users</span>
  <span class="member" style="left:21px;top:29px">Ravi Menon</span><span class="member" style="left:122px;top:29px">Karim Haddad</span>
  <span class="member" style="left:21px;top:51px">Ravi Menon</span><span class="member" style="left:122px;top:51px">Ravi Menon</span>
  <span class="member" style="left:21px;top:73px">Anil</span>
  <span class="member-link">View Complete Members List</span>
</section>
<section class="member-box" style="left:276px">
  <span class="member-tab">Most Active Users (5)</span>
  <span class="member" style="left:21px;top:29px">Ravi Menon</span><span class="member" style="left:122px;top:29px">Karim Haddad</span>
  <span class="member" style="left:21px;top:51px">Ravi Menon</span><span class="member" style="left:122px;top:51px">Ravi Menon</span>
  <span class="member" style="left:21px;top:73px">Anil</span>
  <span class="member-link">View Complete Members List</span>
</section>
<section class="member-box" style="left:514px">
  <span class="member-tab">Most Viewed Articles (5)</span>
  <span class="member" style="left:21px;top:29px">Ravi Menon</span><span class="member" style="left:122px;top:29px">Karim Haddad</span>
  <span class="member" style="left:21px;top:51px">Ravi Menon</span><span class="member" style="left:122px;top:51px">Ravi Menon</span>
  <span class="member" style="left:21px;top:73px">Anil</span>
  <span class="member-link">View more</span>
</section>
<section class="member-box" style="left:752px">
  <span class="member-tab hot">Most Article Comments</span>
  <span class="member" style="left:21px;top:29px">Ravi Menon</span><span class="member" style="left:122px;top:29px">Karim Haddad</span>
  <span class="member" style="left:21px;top:51px">Ravi Menon</span><span class="member" style="left:122px;top:51px">Ravi Menon</span>
  <span class="member" style="left:21px;top:73px">Anil</span>
  <span class="member-link">View more</span>
</section>

<footer class="site-footer">
  <div class="footer-links">Home<span>|</span>About<span>|</span>Hotels<span>|</span>Weather<span>|</span>Maps<span>|</span>Currency Converter<span>|</span>Contact<span>|</span>Privacy Policy<span>|</span>About Our Ads<span>|</span>Terms of Service<span>|</span>Sitemap</div>
  <div class="copyright">Copyright © 2012 Kelmor . All rights reserved.</div>
</footer>

</body>
</html>
```